Lumora Learning Web Design Project

Who We are:
Lumora Learning is education information portal/ magazine, providing information about the Chinese and International education markets. Our aim is to help school principals improve there curriculum, and parents in understanding this curriculum.

Project Brief:
The site will include education news updates, educational services, curriculum developments and overseas study. We hope the site represents the cross cultural bridge between the west and east. The site will cover both the Sciences and Arts.

Note:
The logo design competition is also underway so we only need the website design

What We want:
This competition is for Design only no coding!
Design a home page based on Template 1,2 or 3. I only need to select one.
The design of an article page.

Optional
Design a Microsoft Windows metro style splash page.

Sites We like:
http://www.kavelin.com.cn/kavelinlingo/default.aspx
http://www.brixtalacademia.co.uk/
http://qrpv.norvatestudio.net/

Template Explanations:
Template 1-
The main information has a dynamic sliding category view that when clicked displays the relevant info.
In addition to the main upper menu it also has a left hand sliding menu that pops out on click or gesture

Template 2-
Has limited number of Articles most of the menus are drop downs from the top menu

Template 3-
No Top menu

Target Market(s)

Teachers, principals and parents

Industry/Entity Type

Education

Requirements
Should not have
• kindergarten preschool feel

```html
<!DOCTYPE html>
<html lang="en">
<head>
<meta charset="utf-8">
<title>Lumora Learning – Home</title>
<link href="https://fonts.googleapis.com/css2?family=Open+Sans:wght@400;600;700&family=Oswald:wght@500&display=swap" rel="stylesheet">
<style>
:root{
  --red:#d8292f;
  --red-dark:#b51c22;
  --navy:#1d4677;
  --blue:#114a8b;
  --text:#6d6d6d;
  --light:#f3f3f3;
  --rule:#dedede;
  --white:#fff;
}
*{margin:0;padding:0;box-sizing:border-box}
html,body{width:778px;height:1200px;overflow:hidden;background:var(--white)}
body{position:relative;font-family:"Open Sans",Arial,sans-serif;color:var(--text)}
.abs{position:absolute}
.header{left:0;top:0;width:778px;height:90px;background:linear-gradient(#fbfbfb,#f1f1f1)}
.brand{left:88px;top:48px;display:flex;align-items:center;gap:7px;font-size:15px;font-weight:700;color:var(--navy)}
.brand-dot{width:18px;height:18px;border-radius:50%;background:var(--red)}
.toplinks{right:85px;top:13px;font-size:8px;color:#666}
.toplinks span{margin:0 5px}
.search{left:551px;top:46px;width:143px;height:20px;border:1px solid #ccc;border-radius:10px;background:#fff;font-size:7px;font-style:italic;color:#aaa;padding:4px 10px}
.search svg{position:absolute;right:6px;top:3px}
.nav{left:84px;top:97px;width:610px;height:28px;border-radius:14px;background:linear-gradient(#e4373c,var(--red-dark));border:2px solid #f0b8ba;box-shadow:0 0 0 1px var(--red-dark);display:flex;justify-content:space-between;align-items:center;padding:0 13px;font-size:8px;font-weight:600;color:#fff}
.hero{left:84px;top:129px;width:610px;height:247px;border-radius:18px;overflow:hidden;background:linear-gradient(90deg,#cfdcca 0%,#b9c9b6 35%,#8d8f86 60%,#b1a39a 100%)}
.hero h1{position:absolute;left:18px;top:76px;font-weight:400;font-size:26px;line-height:27px;color:var(--navy)}
.arrows{position:absolute;left:20px;top:202px;display:flex;gap:5px}
.arrow{width:20px;height:20px;border-radius:50%;background:#fff;box-shadow:0 1px 2px rgba(0,0,0,.4);display:flex;align-items:center;justify-content:center}
.rule{height:5px;background:repeating-linear-gradient(45deg,#e3e3e3 0 2px,#cfcfcf 2px 3px)}
.sec-title{font-family:"Oswald",sans-serif;font-weight:500;font-size:14px;line-height:20px;color:var(--red)}
.mini-arrows{display:flex;gap:4px}
.mini{width:13px;height:13px;border-radius:50%;border:1px solid #999;background:#fafafa;display:flex;align-items:center;justify-content:center}
.card{width:178px}
.card .photo{height:95px;border:1px solid #ddd;padding:2px;background:#fff}
.card .photo div{height:100%}
.card h3{margin-top:12px;max-width:168px;font-size:9.5px;line-height:13px;font-weight:700;color:var(--navy)}
.card p{margin-top:8px;font-size:7.3px;line-height:13px}
.box{background:var(--light);border-radius:3px}
.cats{list-style:none;font-size:7.5px;color:#555}
.cats li{height:18.2px;display:flex;align-items:center;gap:8px}
.more{font-size:8px;font-weight:700;color:var(--navy)}
.tweets{position:relative}
.tweet{position:absolute;left:16px;width:163px;height:64px;display:flex;gap:12px;padding-top:5px;border-bottom:1px solid #e2e2e2}
.tweet.last{border-bottom:0}
.avatar{width:42px;height:42px;background:#fff;border:1px solid #ddd;flex:none;display:flex;align-items:center;justify-content:center}
.avatar i{width:22px;height:22px;border-radius:50%;background:var(--red)}
.tweet b{display:block;font-size:10px;font-weight:600;color:var(--navy);line-height:13px}
.tweet span{display:block;font-size:7.5px;line-height:13px;color:#555}
.tweet em{display:block;font-size:7.5px;line-height:12px;color:var(--red)}
.jobs{display:flex;justify-content:space-between;width:610px}
.job{width:112px;height:63px;border:1px solid #ccc;display:flex;align-items:center;justify-content:center;text-align:center;font-size:8.5px;font-weight:600;color:var(--navy);padding:0 8px;line-height:11px}
.footer{left:0;top:1029px;width:778px;height:122px;background:var(--blue);color:#fff}
.footer h4{font-size:9px;font-weight:600;position:absolute;top:13px}
.links{position:absolute;list-style:none;font-size:7.8px;color:#d6e2f0}
.links li{height:16.3px;display:flex;align-items:center;gap:8px}
.links li::before{content:"›";color:var(--red);font-size:10px;font-weight:700}
.email{position:absolute;left:447px;top:30px;width:131px;height:19px;border-radius:3px;background:#3b6fa8;font-size:7.5px;color:#c5d5e8;padding:4px 8px}
.signup{position:absolute;left:532px;top:59px;width:47px;height:18px;border-radius:3px;background:var(--red);font-size:7.5px;font-weight:600;text-align:center;line-height:18px}
.social{position:absolute;left:620px;top:26px;list-style:none;font-size:7.8px;color:#d6e2f0}
.social li{height:16.3px;display:flex;align-items:center;gap:6px}
.social i{width:10px;height:10px;background:#e9eef5;border-radius:1px}
.social li.rss i{background:#f39a1f}
.bottom{left:0;top:1151px;width:778px;height:49px;background:#f4f4f4}
.mini-brand{position:absolute;left:84px;top:12px;width:56px;font-size:5.5px;font-weight:700;color:var(--navy);display:flex;flex-direction:column;align-items:center;gap:3px;line-height:7px;white-space:nowrap}
.mini-brand i{width:12px;height:12px;border-radius:50%;background:var(--red)}
.copy{position:absolute;left:144px;top:21px;font-size:7px;color:var(--navy)}
.legal{position:absolute;right:84px;top:21px;font-size:6.3px;color:#666}
.legal span{margin:0 4px}
</style>
</head>
<body>
<header class="abs header">
  <div class="abs brand"><span class="brand-dot"></span>LUMORA LEARNING</div>
  <div class="abs toplinks">Log in<span>|</span>Register<span>|</span>Subscribe<span>|</span>Site Map</div>
  <div class="abs search">Search...
    <svg width="14" height="14" viewBox="0 0 14 14"><circle cx="5.5" cy="5.5" r="4" fill="none" stroke="#1d4677" stroke-width="1.8"/><line x1="8.5" y1="8.5" x2="12.5" y2="12.5" stroke="#1d4677" stroke-width="2.2" stroke-linecap="round"/></svg>
  </div>
</header>

<nav class="abs nav"><span>HOME</span><span>NEWS</span><span>COMMENTS</span><span>EDUCATION</span><span>FEATURES</span><span>ARTICLES</span><span>BOOKS</span><span>JOBS</span><span>SUBSCRIBE</span><span>CONTACT US</span></nav>

<section class="abs hero" role="img" aria-label="Photo of smiling students holding books outdoors">
  <h1>We are and Education<br>Information<br>Portal...</h1>
  <div class="arrows">
    <div class="arrow"><svg width="8" height="8" viewBox="0 0 8 8"><path d="M5.5 1 2.5 4l3 3" fill="none" stroke="#333" stroke-width="1.5"/></svg></div>
    <div class="arrow"><svg width="8" height="8" viewBox="0 0 8 8"><path d="M2.5 1 5.5 4l-3 3" fill="none" stroke="#333" stroke-width="1.5"/></svg></div>
  </div>
</section>

<!-- Articles -->
<div class="abs rule" style="left:84px;top:404px;width:387px"></div>
<h2 class="abs sec-title" style="left:84px;top:416px">ARTICLES</h2>
<div class="abs mini-arrows" style="left:440px;top:419px">
  <div class="mini"><svg width="5" height="5" viewBox="0 0 5 5"><path d="M4 0 1 2.5 4 5z" fill="#222"/></svg></div>
  <div class="mini"><svg width="5" height="5" viewBox="0 0 5 5"><path d="M1 0 4 2.5 1 5z" fill="#222"/></svg></div>
</div>
<article class="abs card" style="left:84px;top:441px">
  <div class="photo"><div role="img" aria-label="Photo of two students studying with a laptop" style="background:linear-gradient(90deg,#a89a8f,#cfc8c3 50%,#9a8f8a)"></div></div>
  <h3>Nam fermentum vestibulum purus id aliquet....</h3>
  <p>Ut et scelerisque ante. Donec erat purus, faucibus vitae congue vel, porttitor nec lectus. Aenean a nibh eget turpis vehicula tempus ac sed massa. Vestibulum dolor nulla, ultrices ac tincidunt sed, laoreet non est.</p>
</article>
<article class="abs card" style="left:292px;top:441px">
  <div class="photo"><div role="img" aria-label="Photo of a smiling student outdoors" style="background:linear-gradient(90deg,#2f3a2a,#6d6a55 45%,#a8927c 70%,#4c4a3e)"></div></div>
  <h3>Nam fermentum vestibulum purus id aliquet....</h3>
  <p>Ut et scelerisque ante. Donec erat purus, faucibus vitae congue vel, porttitor nec lectus. Aenean a nibh eget turpis vehicula tempus ac sed massa. Vestibulum dolor nulla, ultrices ac tincidunt sed, laoreet non est.</p>
</article>

<!-- Books & Peoples -->
<div class="abs rule" style="left:84px;top:662px;width:179px"></div>
<div class="abs rule" style="left:292px;top:662px;width:179px"></div>
<h2 class="abs sec-title" style="left:84px;top:674px">BOOKS</h2>
<h2 class="abs sec-title" style="left:292px;top:674px">PEOPLES</h2>
<article class="abs card" style="left:84px;top:698px">
  <div class="photo"><div role="img" aria-label="Photo of stacked books and an open book" style="background:linear-gradient(180deg,#4a3a2c,#8a6a45 45%,#c9b08a 75%,#8a7560)"></div></div>
  <h3>Nam fermentum vestibulum purus id aliquet....</h3>
  <p>Ut et scelerisque ante. Donec erat purus, faucibus vitae congue vel, porttitor nec lectus. Aenean a nibh eget turpis vehicula tempus ac sed massa. Vestibulum dolor nulla, ultrices ac tincidunt sed, laoreet non est.</p>
</article>
<article class="abs card" style="left:292px;top:698px">
  <div class="photo"><div role="img" aria-label="Photo of a group of four students on a blue backdrop" style="background:linear-gradient(90deg,#1c2f7a,#3b52a8 50%,#1d2c6e)"></div></div>
  <h3>Nam fermentum vestibulum purus id aliquet....</h3>
  <p>Ut et scelerisque ante. Donec erat purus, faucibus vitae congue vel, porttitor nec lectus. Aenean a nibh eget turpis vehicula tempus ac sed massa. Vestibulum dolor nulla, ultrices ac tincidunt sed, laoreet non est.</p>
</article>

<!-- Categories -->
<aside class="abs box" style="left:499px;top:404px;width:195px;height:244px;padding:10px 16px">
  <h2 class="sec-title">CATEGORIES</h2>
  <ul class="cats" style="margin-top:5px">
    <li><svg width="7" height="6" viewBox="0 0 7 6"><path d="M.5 3 2.5 5 6.5 .5" fill="none" stroke="#1d4677" stroke-width="1.4"/></svg>Aliquam molestie mi et imperdiet</li>
    <li><svg width="7" height="6" viewBox="0 0 7 6"><path d="M.5 3 2.5 5 6.5 .5" fill="none" stroke="#1d4677" stroke-width="1.4"/></svg>Euismod, dui purus auctor</li>
    <li><svg width="7" height="6" viewBox="0 0 7 6"><path d="M.5 3 2.5 5 6.5 .5" fill="none" stroke="#1d4677" stroke-width="1.4"/></svg>Telluset interdum lacus lectus et ante</li>
    <li><svg width="7" height="6" viewBox="0 0 7 6"><path d="M.5 3 2.5 5 6.5 .5" fill="none" stroke="#1d4677" stroke-width="1.4"/></svg>Sed accumsan sollicitudin</li>
    <li><svg width="7" height="6" viewBox="0 0 7 6"><path d="M.5 3 2.5 5 6.5 .5" fill="none" stroke="#1d4677" stroke-width="1.4"/></svg>Sapien sit amet adipiscing</li>
    <li><svg width="7" height="6" viewBox="0 0 7 6"><path d="M.5 3 2.5 5 6.5 .5" fill="none" stroke="#1d4677" stroke-width="1.4"/></svg>Turpis gravida ac</li>
    <li><svg width="7" height="6" viewBox="0 0 7 6"><path d="M.5 3 2.5 5 6.5 .5" fill="none" stroke="#1d4677" stroke-width="1.4"/></svg>Euismod, dui purus auctor</li>
    <li><svg width="7" height="6" viewBox="0 0 7 6"><path d="M.5 3 2.5 5 6.5 .5" fill="none" stroke="#1d4677" stroke-width="1.4"/></svg>Telluset interdum lacus lectus et ante</li>
    <li><svg width="7" height="6" viewBox="0 0 7 6"><path d="M.5 3 2.5 5 6.5 .5" fill="none" stroke="#1d4677" stroke-width="1.4"/></svg>Sed accumsan sollicitudin</li>
    <li><svg width="7" height="6" viewBox="0 0 7 6"><path d="M.5 3 2.5 5 6.5 .5" fill="none" stroke="#1d4677" stroke-width="1.4"/></svg>Sapien sit amet adipiscing</li>
  </ul>
  <div class="more" style="text-align:right;margin-top:6px">VIEW ALL</div>
</aside>

<!-- Recent tweets -->
<aside class="abs box" style="left:499px;top:660px;width:195px;height:246px">
  <h2 class="abs sec-title" style="left:16px;top:8px">RECENT TWEETS</h2>
  <div class="tweet" style="top:30px"><div class="avatar"><i></i></div><div><b>Lumora Learning</b><span>Vestibulum vel metus sit amet turpis bibendum tincidunt..</span><em>Posted on 3 days ago</em></div></div>
  <div class="tweet" style="top:94px"><div class="avatar"><i></i></div><div><b>Lumora Learning</b><span>Vestibulum vel metus sit amet turpis bibendum tincidunt..</span><em>Posted on 3 days ago</em></div></div>
  <div class="tweet last" style="top:158px"><div class="avatar"><i></i></div><div><b>Lumora Learning</b><span>Vestibulum vel metus sit amet turpis bibendum tincidunt..</span><em>Posted on 3 days ago</em></div></div>
  <div class="abs more" style="left:16px;top:226px">READ ALL</div>
</aside>

<!-- Featured jobs -->
<div class="abs rule" style="left:84px;top:915px;width:610px"></div>
<h2 class="abs sec-title" style="left:84px;top:927px">FEATURED JOBS</h2>
<div class="abs mini-arrows" style="left:663px;top:930px">
  <div class="mini"><svg width="5" height="5" viewBox="0 0 5 5"><path d="M4 0 1 2.5 4 5z" fill="#222"/></svg></div>
  <div class="mini"><svg width="5" height="5" viewBox="0 0 5 5"><path d="M1 0 4 2.5 1 5z" fill="#222"/></svg></div>
</div>
<div class="abs jobs" style="left:84px;top:953px">
  <div class="job">Harwick College</div>
  <div class="job">University of Eastmoor</div>
  <div class="job">Verano College of the Arts</div>
  <div class="job">Northgate Metropolitan University</div>
  <div class="job">Calder Vale University</div>
</div>

<footer class="abs footer">
  <h4 style="left:85px">QUICK LINKS</h4>
  <ul class="links" style="left:85px;top:26px">
    <li>Aliquam molestie mi et imperdiet</li><li>Euismod, dui purus auctor</li><li>Telluset interdum lacus lectus et ante</li><li>Sed accumsan sollicitudin</li><li>Sapien sit amet adipiscing</li>
  </ul>
  <ul class="links" style="left:257px;top:26px">
    <li>Aliquam molestie mi et imperdiet</li><li>Euismod, dui purus auctor</li><li>Telluset interdum lacus lectus et ante</li><li>Sed accumsan sollicitudin</li><li>Sapien sit amet adipiscing</li>
  </ul>
  <h4 style="left:447px">SUBSCRIBE US</h4>
  <div class="email">Enter Email</div>
  <div class="signup">SIGN UP</div>
  <h4 style="left:620px">CONNECT US</h4>
  <ul class="social">
    <li><i></i>Gathera</li><li><i></i>Chirply</li><li><i></i>Workvine</li><li><i></i>Orbitly</li><li class="rss"><i></i>Rss Feeds</li>
  </ul>
</footer>

<div class="abs bottom">
  <div class="mini-brand"><i></i>LUMORA LEARNING</div>
  <div class="copy">COPYRIGHT © 2013 ALL RIGHT RESERVED</div>
  <div class="legal">HOW TO ADVERTISE<span>|</span>TERMS &amp; CONDITIONS<span>|</span>PRIVACY POLICY<span>|</span>FEEDBACK<span>|</span>COOKIE<span>|</span>POLICY<span>|</span>HELP</div>
</div>
</body>
</html>
```